Security Camera Sign

14” high x 11” wide Color: Blue, Yellow, Black and white

Make the sign vertical
Replace red with blue
WARNING: Black over yellow
These premises are protected by Closed Circuit Television: On white
Images are recorded for crime prevention and public safety. Unauthorized access, theft or vandalism will result in prosecution: On Blue

Target Market(s)

Outdoor commercial building

Industry/Entity Type

Security

Requirements
Nice to have
• I would like the sign stand out. If you need more colors? Thanks Ok

```html
<!DOCTYPE html>
<html lang="en">
<head>
<meta charset="UTF-8">
<title>Security Camera Sign</title>
<link rel="stylesheet" href="https://fonts.googleapis.com/css2?family=Bebas+Neue&display=swap">
<style>
  :root {
    --sign-blue: #03138a;
    --warning-yellow: #e6ef0e;
    --ink-black: #0b0b0b;
    --paper-white: #ffffff;
    --lens-blue: #3b8fe6;
  }
  html, body {
    margin: 0;
    padding: 0;
    width: 947px;
    height: 1200px;
    overflow: hidden;
    background: var(--paper-white);
  }
  .sign {
    position: relative;
    width: 947px;
    height: 1200px;
    background: var(--paper-white);
    font-family: "Bebas Neue", "Oswald", sans-serif;
  }
  .header-band {
    position: absolute;
    left: 21px;
    top: 21px;
    width: 903px;
    height: 268px;
    background: var(--sign-blue);
    border-radius: 50px 50px 0 0;
  }
  .warning-plate {
    position: absolute;
    left: 99px;
    top: 58px;
    width: 700px;
    height: 156px;
    background: var(--warning-yellow);
    border: 4px solid var(--paper-white);
    border-radius: 14px;
    display: flex;
    align-items: center;
    justify-content: center;
  }
  .warning-word {
    margin: 0;
    color: var(--ink-black);
    font-size: 184px;
    line-height: 1;
    letter-spacing: 0.12em;
    padding-left: 0.12em;
    padding-top: 12px;
    font-weight: 400;
  }
  .cctv-notice {
    position: absolute;
    left: 0;
    width: 947px;
    top: 313px;
    margin: 0;
    text-align: center;
    color: var(--ink-black);
    font-size: 63px;
    line-height: 49px;
    font-weight: 400;
  }
  .camera-illustration {
    position: absolute;
    left: 251px;
    top: 439px;
    width: 443px;
    height: 440px;
    border-radius: 10px;
    background: linear-gradient(160deg, #f4f5f8 0%, #e3e6ee 60%, #cfdcf3 100%);
  }
  .footer-band {
    position: absolute;
    left: 21px;
    top: 888px;
    width: 903px;
    height: 282px;
    background: var(--sign-blue);
    border-radius: 0 0 50px 50px;
    display: flex;
    align-items: center;
    justify-content: center;
  }
  .legal-notice {
    margin: 0;
    text-align: center;
    color: var(--paper-white);
    font-size: 67px;
    line-height: 52px;
    font-weight: 400;
    padding-top: 6px;
  }
</style>
</head>
<body>
  <main class="sign">
    <header class="header-band">
      <div class="warning-plate">
        <h1 class="warning-word">WARNING</h1>
      </div>
    </header>

    <p class="cctv-notice">These premises are protected<br>by closed circuit television</p>

    <div class="camera-illustration" role="img" aria-label="Illustration of a wall-mounted CCTV security camera with a blue lens"></div>

    <footer class="footer-band">
      <p class="legal-notice">Images are recorded for crime<br>prevention and public safety.<br>Unauthorized access, theft or<br>vandalism will result in prosecution</p>
    </footer>
  </main>
</body>
</html>
```